Festive Sexy Winter Banner GIF

Make a Banner that will feature on our website www.PlumRelax.com for this Christmas - Maybe a little bit of animation but not overwhelming - Size of banner must be 713 X 70 Pixels and needs to be a .gif so We can just drop it in and it will work site wide

Target Market(s)

Adult

Industry/Entity Type

Adult

Requirements
Must have
• WORDING MUST BE - Plum Relax 1000's of UK Escorts & Massage Parlours
Nice to have
• Slight animation but not too much

```html
<!DOCTYPE html>
<html lang="en">
<head>
<meta charset="utf-8">
<title>Plum Relax – Winter Banner Frames</title>
<link rel="stylesheet" href="https://fonts.googleapis.com/css2?family=DM+Serif+Display&family=Open+Sans:wght@700&family=Quicksand:wght@500&display=swap">
<style>
  :root {
    --stage-bg: #262450;
    --label: #62648f;
    --pink: #d9046f;
    --pink-deep: #b8005c;
    --pink-light: #e8238a;
    --photo-dark: #2a2a2a;
    --photo-mid: #8a8a8a;
    --photo-light: #d8d8d8;
    --ink-white: #ffffff;
    --tag-bg: #000000;
  }
  * { margin: 0; padding: 0; box-sizing: border-box; }
  html, body {
    width: 1200px;
    height: 578px;
    overflow: hidden;
    background: var(--stage-bg);
  }
  .stage {
    position: relative;
    width: 1200px;
    height: 578px;
  }
  .frame-label {
    position: absolute;
    left: 173px;
    font-family: "Open Sans", sans-serif;
    font-weight: 700;
    font-size: 15px;
    letter-spacing: 2.4px;
    color: var(--label);
    line-height: 1;
  }
  .banner {
    position: absolute;
    left: 173px;
    width: 856px;
    height: 84px;
    display: flex;
    overflow: hidden;
  }
  .banner__field {
    position: relative;
    width: 482px;
    height: 100%;
    background:
      radial-gradient(ellipse at 30% 40%, var(--pink-light) 0%, transparent 55%),
      radial-gradient(ellipse at 80% 70%, var(--pink-deep) 0%, transparent 60%),
      var(--pink);
  }
  .banner__photo {
    width: 374px;
    height: 100%;
    background: linear-gradient(90deg,
      var(--photo-dark) 0%,
      var(--photo-mid) 22%,
      var(--photo-light) 50%,
      var(--photo-mid) 78%,
      var(--photo-dark) 100%);
  }
  .brand-name {
    position: absolute;
    left: 0;
    width: 482px;
    top: 50%;
    transform: translateY(-52%);
    text-align: center;
    font-family: "DM Serif Display", serif;
    font-size: 56px;
    line-height: 1;
    color: var(--ink-white);
  }
  .tagline {
    position: absolute;
    left: 26px;
    top: 29px;
    width: 455px;
    height: 32px;
    background: var(--tag-bg);
    color: var(--ink-white);
    font-family: "Quicksand", sans-serif;
    font-weight: 500;
    font-size: 20px;
    line-height: 32px;
    padding-left: 16px;
    white-space: nowrap;
  }
</style>
</head>
<body>
  <main class="stage">
    <p class="frame-label" style="top:82px">FRAME 1</p>
    <section class="banner" style="top:109px">
      <div class="banner__field">
        <h1 class="brand-name">Plum Relax</h1>
      </div>
      <div class="banner__photo" role="img" aria-label="Black and white close-up photograph of a woman's lips and dark hair"></div>
    </section>

    <p class="frame-label" style="top:232px">FRAME 2</p>
    <section class="banner" style="top:259px">
      <div class="banner__field"></div>
      <div class="banner__photo" role="img" aria-label="Black and white close-up photograph of a woman's lips and dark hair"></div>
    </section>

    <p class="frame-label" style="top:381px">FRAME 3</p>
    <section class="banner" style="top:408px">
      <div class="banner__field">
        <p class="tagline">1000's of UK Escorts and Massage Parlours</p>
      </div>
      <div class="banner__photo" role="img" aria-label="Black and white close-up photograph of a woman's lips and dark hair"></div>
    </section>
  </main>
</body>
</html>
```